Caldrow Supplies Business Card

Professional business card that stand out to our potential customers. Front and back with clean modern design

Industry/Entity Type

Oil and gas

Contact Information for Business Card

Name, address, website , office phone and cell number

Requirements
Must have
• Editable files for each employee

```html
<!DOCTYPE html>
<html lang="en">
<head>
<meta charset="utf-8">
<title>Caldrow Supplies Business Card</title>
<link rel="stylesheet" href="https://fonts.googleapis.com/css2?family=Open+Sans:wght@400;600;700;800&display=swap">
<style>
  :root {
    --bg: #161616;
    --card: #202020;
    --red: #ff1a1a;
    --blue: #10b2d4;
    --text: #d8d8d8;
  }
  * { margin: 0; padding: 0; box-sizing: border-box; }
  html, body { width: 1200px; height: 801px; overflow: hidden; }
  body {
    background: var(--bg);
    font-family: "Open Sans", Arial, sans-serif;
    position: relative;
  }
  .card {
    position: absolute;
    top: 246px;
    width: 540px;
    height: 309px;
    background: var(--card);
    border-radius: 14px;
    overflow: hidden;
    box-shadow: 0 18px 40px rgba(0,0,0,.55);
  }
  .card--front { left: 40px; }
  .card--back { left: 620px; }

  .front-brand {
    position: absolute;
    inset: 0;
    display: flex;
    align-items: center;
    justify-content: center;
    gap: 14px;
  }
  .brand-square {
    width: 26px; height: 26px;
    background: var(--red);
  }
  .brand-name {
    font-weight: 800;
    color: var(--red);
    letter-spacing: 1.5px;
    text-transform: uppercase;
  }
  .front-brand .brand-name { font-size: 30px; }

  .edge-band { position: absolute; left: 0; width: 9px; }
  .edge-band--red { top: 0; height: 55%; background: var(--red); }
  .edge-band--blue { bottom: 0; height: 45%; background: var(--blue); }

  .back-brand {
    position: absolute;
    top: 34px; right: 34px;
    display: flex; align-items: center; gap: 10px;
  }
  .back-brand .brand-square { width: 18px; height: 18px; }
  .back-brand .brand-name { font-size: 18px; }

  .person {
    position: absolute;
    left: 46px; top: 128px;
  }
  .person__name {
    color: var(--red);
    font-weight: 700;
    font-size: 27px;
    letter-spacing: .5px;
    line-height: 1.1;
  }
  .person__title {
    color: var(--blue);
    font-size: 14px;
    margin-top: 2px;
  }
  .divider {
    position: absolute;
    left: 46px; right: 30px; top: 193px;
    height: 1px;
    background: var(--red);
  }
  .contacts {
    position: absolute;
    left: 46px; top: 204px;
    list-style: none;
    color: var(--text);
    font-size: 12.5px;
    line-height: 21px;
  }
  .contacts li { display: flex; align-items: center; gap: 9px; }
  .contacts svg { width: 12px; height: 12px; fill: var(--blue); flex: none; }

  .company {
    position: absolute;
    right: 30px; top: 204px;
    text-align: right;
    color: var(--text);
    font-size: 12.5px;
    line-height: 21px;
  }
  .company__badge {
    display: inline-block;
    color: var(--red);
    font-weight: 800;
    font-size: 11px;
    letter-spacing: 1px;
    text-transform: uppercase;
    margin-bottom: 2px;
  }
</style>
</head>
<body>
  <section class="card card--front" aria-label="Card front">
    <div class="front-brand">
      <span class="brand-square"></span>
      <span class="brand-name">Caldrow Supplies</span>
    </div>
  </section>

  <section class="card card--back" aria-label="Card back">
    <span class="edge-band edge-band--red"></span>
    <span class="edge-band edge-band--blue"></span>

    <div class="back-brand">
      <span class="brand-square"></span>
      <span class="brand-name">Caldrow Supplies</span>
    </div>

    <div class="person">
      <h1 class="person__name">DANIEL HARPER</h1>
      <p class="person__title">Founder &amp; CEO</p>
    </div>

    <div class="divider"></div>

    <ul class="contacts">
      <li><svg viewBox="0 0 24 24"><path d="M6.6 10.8a15 15 0 0 0 6.6 6.6l2.2-2.2a1 1 0 0 1 1-.25 11.4 11.4 0 0 0 3.6.57 1 1 0 0 1 1 1V20a1 1 0 0 1-1 1A17 17 0 0 1 3 4a1 1 0 0 1 1-1h3.5a1 1 0 0 1 1 1c0 1.25.2 2.45.57 3.57a1 1 0 0 1-.25 1z"/></svg>(123) 456-7890</li>
      <li><svg viewBox="0 0 24 24"><path d="M7 1h10a2 2 0 0 1 2 2v18a2 2 0 0 1-2 2H7a2 2 0 0 1-2-2V3a2 2 0 0 1 2-2zm0 3v14h10V4zm5 15.5a1 1 0 1 0 0 2 1 1 0 0 0 0-2z"/></svg>(123) 456-7890</li>
      <li><svg viewBox="0 0 24 24"><path d="M6 2h12v5H6zM4 8h16a2 2 0 0 1 2 2v7h-4v5H6v-5H2v-7a2 2 0 0 1 2-2zm4 8v4h8v-4z"/></svg>(123) 456-7890</li>
      <li><svg viewBox="0 0 24 24"><path d="M2 5h20v14H2zm2 2v.5l8 5 8-5V7z"/></svg>info@yourwebsitehere.com</li>
    </ul>

    <div class="company">
      <span class="company__badge">Caldrow Supplies</span>
      <p>423 Street Address Here, City</p>
      <p>State &amp; Country, ZIP Code</p>
      <p>www.yourwebsitehere.com</p>
    </div>
  </section>
</body>
</html>
```